KerrLow Farm

Need a nice simple clean double sided business card that has our logo and info on:
Kerr Low Farm
Martin & Felicity Kerr Low
kerrlowfarm@mailbarn.example
Martin: 1-780-555-0148
Felicity: 1-780-555-0193
Instagram @ kerrlow_farm

Contact Information for Business Card

Martin & Felicity Kerr Low kerrlowfarm@mailbarn.example Martin: 1-780-555-0148 Felicity: 1-780-555-0193

```html
<!DOCTYPE html>
<html lang="en">
<head>
<meta charset="utf-8">
<title>Kerr Low Farm – Business Card</title>
<link href="https://fonts.googleapis.com/css2?family=Oswald:wght@300;400;600&display=swap" rel="stylesheet">
<style>
  :root {
    --backdrop: #6f7b88;
    --card: #ffffff;
    --green: #5a9a2c;
    --ink: #1d1d1d;
    --field-gold: #c9a452;
    --hedge: #4f6e34;
    --haze: #e9e4cf;
  }
  html, body {
    margin: 0;
    width: 1200px;
    height: 876px;
    overflow: hidden;
    background: var(--backdrop);
    font-family: "Oswald", "Arial Narrow", sans-serif;
  }
  .card {
    position: absolute;
    left: 100px;
    top: 152px;
    width: 1000px;
    height: 571px;
    background: var(--card);
    overflow: hidden;
    box-shadow: 0 6px 18px rgba(0,0,0,0.25);
  }
  .field-photo {
    position: absolute;
    inset: 0;
    background:
      radial-gradient(ellipse at 38% 22%, var(--haze) 0%, transparent 40%),
      linear-gradient(160deg, var(--hedge) 0%, #7b8a4a 30%, var(--field-gold) 60%, #a9823c 100%);
    -webkit-mask-image: linear-gradient(100deg, #000 0%, #000 38%, transparent 66%);
    mask-image: linear-gradient(100deg, #000 0%, #000 38%, transparent 66%);
  }
  .brand {
    position: absolute;
    left: 580px;
    top: 34px;
    width: 360px;
    text-align: center;
  }
  .brand-dot {
    display: block;
    width: 84px; height: 84px;
    margin: 0 auto 12px;
    border: 4px solid var(--green);
    border-radius: 50%;
    box-sizing: border-box;
  }
  .brand-name {
    font-size: 38px;
    font-weight: 400;
    color: var(--green);
    letter-spacing: 1px;
    text-transform: uppercase;
    line-height: 1;
  }
  .contact {
    position: absolute;
    left: 600px;
    top: 218px;
    color: var(--ink);
  }
  .owners {
    margin: 0;
    font-size: 26px;
    font-weight: 600;
    color: var(--green);
    text-transform: uppercase;
    line-height: 1.1;
  }
  .farm {
    margin: 2px 0 24px;
    font-size: 17px;
    font-weight: 400;
  }
  .line {
    display: flex;
    align-items: center;
    gap: 10px;
    font-size: 18px;
    font-weight: 300;
    margin-bottom: 10px;
  }
  .line svg { width: 18px; height: 18px; flex: none; }
  .icon-phone { fill: var(--green); }
  .web {
    margin-top: 6px;
    font-size: 18px;
    font-weight: 400;
    color: var(--green);
  }
</style>
</head>
<body>
  <div class="card">
    <div class="field-photo" role="img" aria-label="Photo of two tractors baling hay in a sunlit field beside a green hedgerow"></div>

    <div class="brand">
      <span class="brand-dot"></span>
      <div class="brand-name">Kerr Low Farm</div>
    </div>

    <div class="contact">
      <h1 class="owners">Martin &amp; Felicity Kerr Low</h1>
      <p class="farm">Kerr Low Farm</p>
      <div class="line">
        <svg class="icon-phone" viewBox="0 0 24 24" aria-hidden="true"><path d="M6.6 10.8a15 15 0 0 0 6.6 6.6l2.2-2.2a1 1 0 0 1 1-.25 11.4 11.4 0 0 0 3.6.57 1 1 0 0 1 1 1V20a1 1 0 0 1-1 1A17 17 0 0 1 3 4a1 1 0 0 1 1-1h3.5a1 1 0 0 1 1 1c0 1.25.2 2.45.57 3.57a1 1 0 0 1-.25 1z"/></svg>
        <span>martin: 1-780-555-0148</span>
      </div>
      <div class="line">
        <svg class="icon-phone" viewBox="0 0 24 24" aria-hidden="true"><path d="M6.6 10.8a15 15 0 0 0 6.6 6.6l2.2-2.2a1 1 0 0 1 1-.25 11.4 11.4 0 0 0 3.6.57 1 1 0 0 1 1 1V20a1 1 0 0 1-1 1A17 17 0 0 1 3 4a1 1 0 0 1 1-1h3.5a1 1 0 0 1 1 1c0 1.25.2 2.45.57 3.57a1 1 0 0 1-.25 1z"/></svg>
        <span>felicity: 1-780-555-0193</span>
      </div>
      <div class="line">
        <svg viewBox="0 0 24 24" aria-hidden="true"><rect x="2" y="5" width="20" height="14" fill="#5a9a2c"/><path d="M3 6l9 7 9-7" fill="none" stroke="#fff" stroke-width="1.8"/></svg>
        <span>kerrlowfarm@mailbarn.example</span>
      </div>
      <div class="web">www.fieldnotes.example/kerrlow_farm</div>
    </div>
  </div>
</body>
</html>
```